Harbor Lane Consignment Brochure

We need a brochure to showcase our consignment business. We are a company that sells event tickets (sports, concerts, theatre, etc...) on the secondary market. We are now starting a new business venture where other companies like ours can sell through us, leveraging our technology, and our infrastructure to grow their business.

We want to showcase the benefits of consigning with us, instead of doing things on your own. By using our services companies won't have to deal with providing customer support, packaging and delivering tickets, fighting credit card charge-backs. They also won't need to pay for expensive software utilities, point-of-sale licenses, and exchange fees. (An exchange is where they list tickets, like SeatLoop.com or PassQuick.com).
Updates

We've decided we have to scrap the testimonials page, so instead of testimonials, let's go with this: OUR PROMISE TO YOU: The best automation software in the industry. Incredibly fast and accurate pricing. Exposure on every major and minor exchange. Real time sales data on your desktop or phone. Earlier sales for more money. Constantly updated technology and outstanding support. Top-notch staff handling all customer service. On-time packaging and delivery. All while meeting or beating your current exchange rates!

Target Market(s)

We want to advertise that by using our services we'll meet or beat their current rates on the various exchanges (SeatLoop, GateMarketry, PassQuick, etc...) and save them money by eliminating their need for expensive software and extra labor.
We want to target 2 key demographics.

The first is smaller brokers that do maybe $300k-$500k in annual sales. For these brokers the monthly and yearly expenses of automation software, point-of-sale systems, and website hosting can eat into a large part of their profit. A small time broker could save over $15,000 / year in those expenses alone.

The second target is larger brokers that do several million in annual sales. For these brokers, they're paying for labor to package and deliver tickets (shipping and handling), answer phones and resolve issues (customer support), fight credit card charge-backs. They're also paying for the infrastructure of supporting an office: rent, utilities, etc... A large broker like this could save hundreds of thousands of dollars by reducing their need for all that labor, which would in turn reduce their need for a large office space

Industry/Entity Type

Credit Card

Requirements
Must have
• Tri-fold layout
Use the logo provided (if you need .AI or .PSD version of it I can provide them)
Color-schema that fits well with the logo
Website URL: www.harborlaneconsignment.example
Contact Email: contact@harborlaneconsignment.example
Nice to have
• I would like the a page focused on the smaller brokers and another page focused on the larger brokers (based on the information provided previously)

```html
<!DOCTYPE html>
<html lang="en">
<head>
<meta charset="utf-8">
<title>Harbor Lane Consignment Brochure</title>
<link href="https://fonts.googleapis.com/css2?family=Lato:wght@300;400;700;900&family=Dosis:wght@800&display=swap" rel="stylesheet">
<style>
  :root {
    --navy: #2b3990;
    --ribbon: #2f80cf;
    --sky: #2a82d6;
    --sky-deep: #1f68b8;
    --ink: #111111;
    --white: #ffffff;
    --green: #2fae49;
    --green-soft: #3cb54e;
    --red: #e3262b;
    --ticket: #e7e5dc;
    --orange: #f08a5d;
    --gold: #e8c547;
  }
  * { box-sizing: border-box; margin: 0; padding: 0; }
  html, body { width: 1200px; height: 737px; overflow: hidden; background: var(--white); }
  body { font-family: "Lato", Arial, sans-serif; color: var(--ink); }
  .brochure { position: relative; width: 1200px; height: 737px; overflow: hidden; }
  .panel { position: absolute; top: 0; height: 737px; }
  .panel--about { left: 0; width: 405px; }
  .panel--tech { left: 405px; width: 393px; background: linear-gradient(180deg, #3a8fde 0%, var(--sky) 50%, var(--sky-deep) 100%); }
  .panel--overhead { left: 798px; width: 402px; }
  .abs { position: absolute; }
  .center { text-align: center; }

  .ribbon { position: absolute; left: 0; top: 0; }

  .section-icon { position: absolute; border-radius: 6px; }
  .section-title { position: absolute; color: var(--navy); font-weight: 700; font-size: 21px; text-align: center; width: 300px; }
  .section-copy { position: absolute; font-size: 13.5px; line-height: 17.6px; text-align: center; }

  .tech-heading, .overhead-heading { position: absolute; top: 108px; width: 100%; text-align: center; font-size: 21px; line-height: 25px; }
  .tech-heading .light, .overhead-heading .light { font-weight: 400; display: block; }
  .tech-heading .bold, .overhead-heading .bold { font-weight: 900; display: block; }
  .overhead-heading { color: var(--green); }
  .intro { position: absolute; top: 174px; font-size: 13.5px; line-height: 17.6px; text-align: center; }

  .cost-label { position: absolute; color: var(--white); font-weight: 700; font-size: 10.5px; line-height: 10px; }
  .cost-price { position: absolute; color: var(--white); font-size: 11px; }
  .cost-icon { position: absolute; }
  .laptop { position: absolute; left: 143px; top: 333px; width: 108px; height: 72px; border-radius: 4px; background: linear-gradient(180deg, #f2f4f7, #c9ced6); }
  .grand-total { position: absolute; top: 470px; width: 100%; text-align: center; font-size: 20px; font-weight: 300; }
  .closing { position: absolute; top: 512px; left: 12px; width: 369px; text-align: center; font-size: 18px; line-height: 23.5px; font-weight: 900; }

  .expense-list { position: absolute; top: 291px; left: 20px; list-style: none; font-size: 12.5px; line-height: 17px; }
  .expense-list li { display: flex; align-items: center; }
  .expense-list svg { margin-right: 5px; }
  .expense-list .item { width: 200px; }
  .savings { position: absolute; top: 360px; left: 20px; width: 362px; text-align: center; color: var(--green-soft); font-weight: 300; font-size: 18.5px; line-height: 24px; }

  .cta { position: absolute; left: 22px; top: 490px; width: 355px; height: 122px; }
  .cta-text { position: absolute; left: 0; width: 355px; text-align: center; font-family: "Dosis", "Arial Narrow", sans-serif; font-weight: 800; font-size: 29px; letter-spacing: 0.5px; }
  .cta-title { top: 28px; color: var(--green); }
  .cta-phone { top: 62px; color: var(--navy); }
  .cta-phone .call { color: var(--red); }
</style>
</head>
<body>
<main class="brochure">

  <section class="panel panel--about">
    <svg class="ribbon" width="150" height="150" viewBox="0 0 150 150" aria-hidden="true">
      <polygon points="0,108 108,0 148,0 0,148" fill="var(--ribbon)"/>
      <circle cx="8" cy="118" r="4" fill="var(--white)"/>
      <circle cx="118" cy="8" r="4" fill="var(--white)"/>
      <text x="64" y="68" transform="rotate(-45 64 64)" text-anchor="middle" fill="var(--white)" font-family="Lato, Arial, sans-serif" font-weight="900" font-size="15" letter-spacing="1">ABOUT US</text>
    </svg>

    <div class="section-icon" role="img" aria-label="Pair of admission tickets illustration" style="left:188px;top:52px;width:50px;height:48px;background:var(--orange);transform:rotate(-12deg);"></div>
    <h2 class="section-title" style="left:67px;top:107px;">Who We Are</h2>
    <p class="section-copy" style="left:65px;top:136px;width:304px;">We are an industry-leading ticket broker in business for almost 30 years. We're now offering our efficiency and expertise to select members of the broker community as a consignment service.</p>

    <div class="section-icon" role="img" aria-label="Open shipping box illustration" style="left:184px;top:230px;width:50px;height:48px;background:linear-gradient(180deg,#6fc1a8 0%,#6fc1a8 35%,var(--gold) 35%);"></div>
    <h2 class="section-title" style="left:67px;top:288px;">What We Do</h2>
    <p class="section-copy" style="left:62px;top:314px;width:310px;">We sell tickets. Lots of them! Using a combination of industry standard and proprietary software and an amazing staff we handle all of the receiving, downloading, scanning, packaging, shipping, uploading, and customer service, so you can do what you do best: buy and sell more tickets!</p>

    <div class="section-icon" role="img" aria-label="Web browser icons" style="left:182px;top:443px;width:58px;height:44px;border-radius:22px;background:linear-gradient(90deg,#e0553f,#f4a340,#3d8fd8);"></div>
    <h2 class="section-title" style="left:67px;top:494px;">How It Works</h2>
    <p class="section-copy" style="left:70px;top:520px;width:294px;">Using our web-based portal you can access our system from anywhere in the world to buy-in and price your inventory. We list your tickets on every major ticket exchange at a rate that matches or beats your current rate. When your tickets arrive you send them, in bulk, to our offices and we handle the rest. You receive payment twice a month for all tickets that have been sold and delivered.</p>
  </section>

  <section class="panel panel--tech">
    <h2 class="tech-heading"><span class="light">LEVERAGE OUR TECHNOLOGY</span><span class="bold">SAVE THOUSANDS!</span></h2>
    <p class="intro" style="left:16px;width:361px;">To compete in today's market you need every technological advantage possible. You could spend thousands every year on expensive automation software, point of sale systems, web hosting, server hosting, point-of-sale systems, and exchange fees – or you could consign with us and enjoy all those benefits without the hefty price tag.</p>

    <div class="cost-label" style="left:15px;top:308px;">POINT-OF-SALE<br>SYSTEM</div>
    <div class="cost-price" style="left:38px;top:335px;">$2,400/year</div>
    <svg class="cost-icon" style="left:101px;top:321px;" width="32" height="32" viewBox="0 0 32 32" aria-hidden="true">
      <circle cx="16" cy="16" r="15" fill="var(--white)"/>
      <rect x="9" y="10" width="14" height="10" fill="none" stroke="var(--sky)" stroke-width="2"/>
      <rect x="13" y="21" width="6" height="2" fill="var(--sky)"/>
    </svg>

    <div class="laptop" role="img" aria-label="Laptop showing the consignment portal"></div>

    <div class="cost-label" style="left:296px;top:308px;">AUTOMATION<br>SOFTWARE</div>
    <div class="cost-price" style="left:296px;top:336px;">$4,500/year</div>
    <svg class="cost-icon" style="left:258px;top:321px;" width="32" height="32" viewBox="0 0 32 32" aria-hidden="true">
      <circle cx="16" cy="16" r="15" fill="var(--white)"/>
      <path d="M11 9v14M16 9v14M21 9v14" stroke="var(--sky)" stroke-width="2"/>
      <path d="M9 13h4M14 18h4M19 12h4" stroke="var(--sky)" stroke-width="2"/>
    </svg>

    <div class="cost-label" style="left:15px;top:406px;">EXCHANGE FEES</div>
    <div class="cost-price" style="left:42px;top:422px;">$5,700/year</div>
    <svg class="cost-icon" style="left:100px;top:406px;" width="32" height="32" viewBox="0 0 32 32" aria-hidden="true">
      <circle cx="16" cy="16" r="15" fill="var(--white)"/>
      <text x="16" y="21" text-anchor="middle" fill="var(--sky)" font-family="Lato, Arial, sans-serif" font-size="14">$</text>
    </svg>

    <div class="cost-label" style="left:290px;top:395px;">WEBSITE / SERVER<br>INFRASTRUCTURE</div>
    <div class="cost-price" style="left:292px;top:424px;">$3,000/year</div>
    <svg class="cost-icon" style="left:254px;top:407px;" width="32" height="32" viewBox="0 0 32 32" aria-hidden="true">
      <circle cx="16" cy="16" r="15" fill="var(--white)"/>
      <path d="M16 23l-6-6a3.5 3.5 0 0 1 6-4 3.5 3.5 0 0 1 6 4z" fill="var(--sky)"/>
    </svg>

    <p class="grand-total">Grand Total: Over $15,000/year!</p>
    <p class="closing">That's money you could spend on growing your business or better enjoying all the free time you'll have while we take care of the day-to-day operations.</p>
  </section>

  <section class="panel panel--overhead">
    <h2 class="overhead-heading"><span class="light">LOWER YOUR OVERHEAD</span><span class="bold">GROW YOUR BUSINESS!</span></h2>
    <p class="intro" style="left:12px;width:380px;">A large broker has a lot of overhead. You need people to assist customers, deal with exchanges, package and ship orders, combat fraud, fight credit card charge-backs, and constantly monitor your inventory to ensure no mistakes are being made. What if you didn't need to worry about all of that extra labor and the overhead associated with it?</p>

    <ul class="expense-list">
      <li><svg width="12" height="12" viewBox="0 0 12 12" aria-hidden="true"><rect x="0.5" y="0.5" width="11" height="11" fill="none" stroke="var(--green)"/><path d="M2.5 6l2.5 2.5 5-6" fill="none" stroke="var(--green)" stroke-width="1.8"/></svg><span class="item">Customer Support &amp; Sales Labor:</span><span>$45,000/person/year</span></li>
      <li><svg width="12" height="12" viewBox="0 0 12 12" aria-hidden="true"><rect x="0.5" y="0.5" width="11" height="11" fill="none" stroke="var(--green)"/><path d="M2.5 6l2.5 2.5 5-6" fill="none" stroke="var(--green)" stroke-width="1.8"/></svg><span class="item">Large Office Lease:</span><span>$40,000/year</span></li>
      <li><svg width="12" height="12" viewBox="0 0 12 12" aria-hidden="true"><rect x="0.5" y="0.5" width="11" height="11" fill="none" stroke="var(--green)"/><path d="M2.5 6l2.5 2.5 5-6" fill="none" stroke="var(--green)" stroke-width="1.8"/></svg><span class="item">IT Support / Infrastructure:</span><span>$30,000/year</span></li>
    </ul>

    <p class="savings">You could save hundreds of thousands in unnecessary overhead and eliminate the headache and stress that comes with running a large brokerage.</p>

    <div class="cta">
      <svg class="abs" width="355" height="122" viewBox="0 0 355 122" aria-hidden="true">
        <rect width="355" height="122" fill="var(--ticket)"/>
        <circle cx="0" cy="61" r="11" fill="var(--white)"/>
        <circle cx="355" cy="61" r="11" fill="var(--white)"/>
        <line x1="18" y1="11" x2="337" y2="11" stroke="var(--white)" stroke-width="2"/>
        <line x1="18" y1="111" x2="337" y2="111" stroke="var(--white)" stroke-width="2"/>
      </svg>
      <p class="cta-text cta-title">FOR MORE INFORMATION</p>
      <p class="cta-text cta-phone"><span class="call">CALL</span> 1-800-555-0142</p>
    </div>
  </section>

</main>
</body>
</html>
```